Marrowind Vodka logo and label design

We would like a logo and bottle label design for a new line of Ultra-Premium Vodka. The Company is called Marrowind Spirits and is based in Brisbane, Australia. We would like a 'Gatsby/Prohibition era vibe to the design. We want to keep it minimalistic and sleek. We strongly prefer a minimalist design and colour palette. Black,Gold,Grey,White,Silver,Red and Blue

The bottle will be similar in shape to Halvorak/Pale Heron. There will also need to be space on the label for required information, as well as short bio of the company, which will be provided to the winning design.

We would like to add the polish code of arms for Opoczno. Have attached link for reference. https://www.crestarchive-demo.net/crestarchive/index.php?title=Opoczno

Target Market(s)

Luxury brand customers

Logo Text

Marrowind Ultra-Premium Vodka

Logo styles of interest
Wordmark Logo
Lettermark Logo
Requirements
Must have
• This is the first release from our new Vodka label. We want a logo and bottle label that reflects a premium product. We very much like Prohibition/Gatsby era themed bottles and labels. The label and bottle should be elegant and clean.
Should not have
• Anything too busy or confusing.

```html
<!DOCTYPE html>
<html lang="en">
<head>
<meta charset="utf-8">
<title>Marrowind Ultra-Premium Vodka – Label</title>
<link rel="stylesheet" href="https://fonts.googleapis.com/css2?family=Oswald:wght@400;500&family=Playfair+Display:wght@500&family=Cinzel:wght@600&family=Libre+Baskerville&display=swap">
<style>
  :root {
    --backdrop: #ecedec;
    --label-white: #fbfbfa;
    --gold: #c6a97f;
    --gold-deep: #b8976a;
    --gold-pale: #efe4d3;
  }
  html, body {
    margin: 0;
    width: 1200px;
    height: 900px;
    overflow: hidden;
    background: var(--backdrop);
  }
  .canvas {
    position: relative;
    width: 1200px;
    height: 900px;
  }
  .label {
    position: absolute;
    left: 340px;
    top: 60px;
    width: 520px;
    height: 780px;
    background: var(--label-white);
    box-shadow: 0 2px 18px rgba(0,0,0,0.06);
    overflow: hidden;
  }
  .branch {
    position: absolute;
    background: linear-gradient(160deg, var(--gold-pale), rgba(239,228,211,0.2));
    opacity: 0.6;
  }
  .branch--left { left: 0; top: 224px; width: 96px; height: 240px; border-radius: 0 48px 48px 0; }
  .branch--right { right: 0; top: 264px; width: 130px; height: 456px; border-radius: 65px 0 0 65px; }
  .wordmark {
    position: absolute;
    top: 130px;
    left: 0;
    width: 100%;
    margin: 0;
    text-align: center;
    font-family: "Oswald", sans-serif;
    font-weight: 500;
    font-size: 60px;
    letter-spacing: 1px;
    color: var(--gold);
    text-transform: uppercase;
    line-height: 1;
  }
  .emblem {
    position: absolute;
    top: 254px;
    left: 247px;
    width: 26px;
    height: 26px;
    background: var(--gold);
  }
  .range {
    position: absolute;
    top: 371px;
    left: 0;
    width: 100%;
    margin: 0;
    text-align: center;
    font-family: "Oswald", sans-serif;
    font-weight: 400;
    font-size: 32px;
    color: var(--gold);
    text-transform: uppercase;
    line-height: 1;
  }
  .product {
    position: absolute;
    top: 411px;
    left: 0;
    width: 100%;
    margin: 0;
    text-align: center;
    font-family: "Playfair Display", serif;
    font-weight: 500;
    font-size: 96px;
    color: var(--gold);
    line-height: 1;
  }
  .origin {
    position: absolute;
    top: 693px;
    left: 120px;
    width: 280px;
    text-align: center;
    color: var(--gold-deep);
  }
  .origin__rule { height: 2px; background: var(--gold); }
  .origin__rule--bottom { margin-top: 4px; }
  .origin__title {
    font-family: "Cinzel", serif;
    font-weight: 600;
    font-size: 19px;
    letter-spacing: 6px;
    margin-top: 5px;
    line-height: 1.1;
  }
  .origin__details {
    font-family: "Libre Baskerville", serif;
    font-size: 12px;
    letter-spacing: 1px;
    line-height: 1.2;
  }
</style>
</head>
<body>
<main class="canvas">
  <section class="label">
    <div class="branch branch--left" role="img" aria-label="Fine gold bare-branch illustration"></div>
    <div class="branch branch--right" role="img" aria-label="Fine gold bare-branch illustration"></div>

    <h1 class="wordmark">Marrowind</h1>
    <div class="emblem" aria-hidden="true"></div>

    <p class="range">Ultra-Premium</p>
    <p class="product">VODKA</p>

    <div class="origin">
      <div class="origin__rule"></div>
      <div class="origin__title">IMPORTED</div>
      <div class="origin__details">alc. 40% vol. 0.75 Lt</div>
      <div class="origin__rule origin__rule--bottom"></div>
    </div>
  </section>
</main>
</body>
</html>
```